Event flyer for Sunday night Youth Group

Need a 4 x 6 or 5 x 7 flyer for a new youth group starting on April 14. The youth group is for students in middle school and high school so it needs to look fun and cool, but not childish. I prefer it not to include pictures of people unless it's so obscure you can't really see their faces. I've uploaded some pictures of flyers I like. I've also attached a couple versions of our logo to use on the flyer.
Information the flyer needs to include:
Youth Group
Sundays, 6-8pm (beginning April 14)
Location: Wexlander's - 4182 Quillon Ridge Ave N, Keizer, 97158
There will be dinner, games, friends, and a message.
Target Market(s)
Youth ages 13-18
Industry/Entity Type
Church
Colors
Look and feel

```html
<!DOCTYPE html>
<html lang="en">
<head>
<meta charset="utf-8">
<title>Youth Group – Harborline Fellowship</title>
<link rel="stylesheet" href="https://fonts.googleapis.com/css2?family=Open+Sans:wght@400;600;700;800&family=Pacifico&family=Montserrat:wght@400;500&display=swap">
<style>
  :root {
    --page-bg: #4a4a4a;
    --paper: #ffffff;
    --slate: #34454f;
    --band: #3b4c56;
    --sage: #7b8b78;
    --sage-edge: #3f5b4d;
    --gold: #e8b42a;
    --amber: #e49a2e;
    --ink: #111111;
    --light: #ffffff;
  }
  * { margin: 0; padding: 0; box-sizing: border-box; }
  html, body {
    width: 1200px; height: 2167px; overflow: hidden;
    background: var(--page-bg);
  }
  .flyer {
    position: absolute; left: 100px; top: 385px;
    width: 1000px; height: 1396px;
    background: var(--paper);
    overflow: hidden;
    box-shadow: 0 10px 30px rgba(0,0,0,.35);
    font-family: 'Open Sans', sans-serif;
    text-align: center;
  }
  .flyer-art { position: absolute; inset: 0; width: 1000px; height: 1396px; }
  .org {
    position: absolute; top: 78px; left: 0; right: 0;
    display: flex; justify-content: center; align-items: center; gap: 18px;
  }
  .org-mark { width: 46px; height: 46px; background: var(--slate); }
  .org-name {
    font-family: 'Montserrat', sans-serif; font-weight: 500;
    font-size: 34px; letter-spacing: 2px; color: var(--slate);
  }
  .title-youth, .title-group {
    position: absolute; left: 0; right: 0;
    font-family: 'Pacifico', cursive; line-height: 1;
  }
  .title-youth {
    top: 170px; font-size: 250px; color: var(--slate);
    text-shadow: 4px 6px 6px rgba(0,0,0,.3);
    padding-right: 20px;
  }
  .title-group {
    top: 420px; font-size: 190px; color: var(--sage);
    -webkit-text-stroke: 6px var(--sage-edge); paint-order: stroke fill;
    text-shadow: 4px 6px 6px rgba(0,0,0,.3);
    padding-left: 60px;
  }
  .schedule {
    position: absolute; top: 712px; left: 0; right: 0;
    font-weight: 800; font-size: 80px; color: var(--ink); line-height: 1;
  }
  .start-date {
    position: absolute; top: 806px; left: 0; right: 0;
    font-weight: 700; font-size: 46px; color: var(--ink); line-height: 1;
  }
  .offer-lead {
    position: absolute; top: 972px; left: 0; right: 0;
    font-weight: 400; font-size: 34px; color: var(--ink);
  }
  .offer-list {
    position: absolute; top: 1018px; left: 0; right: 0;
    font-weight: 700; font-size: 35px; color: var(--ink);
  }
  .phone {
    position: absolute; top: 1262px; left: 0; right: 0;
    font-weight: 800; font-size: 42px; color: var(--light); line-height: 1.1;
  }
  .venue {
    position: absolute; top: 1318px; left: 59px; width: 876px; height: 42px;
    border-radius: 21px; background: var(--sage);
    font-weight: 600; font-size: 30px; color: var(--light); line-height: 42px;
  }
  .site {
    position: absolute; top: 1360px; left: 0; right: 0;
    font-weight: 600; font-size: 25px; color: var(--light);
  }
</style>
</head>
<body>
  <main class="flyer">
    <svg class="flyer-art" viewBox="0 0 1000 1396" aria-hidden="false">
      <defs>
        <linearGradient id="brushFill" x1="0" y1="0" x2="0" y2="1">
          <stop offset="0" stop-color="#e9c62a"/>
          <stop offset="0.55" stop-color="#e8b42a"/>
          <stop offset="1" stop-color="#e49a2e"/>
        </linearGradient>
        <linearGradient id="topBand" x1="0" y1="0" x2="1" y2="0">
          <stop offset="0" stop-color="#eaa52a"/>
          <stop offset="1" stop-color="#f3d36a" stop-opacity=".4"/>
        </linearGradient>
        <radialGradient id="crowdGlow" cx="0.5" cy="0.6" r="0.6">
          <stop offset="0" stop-color="#f6e07a"/>
          <stop offset="0.6" stop-color="#f4d9b0" stop-opacity=".7"/>
          <stop offset="1" stop-color="#ffffff" stop-opacity="0"/>
        </radialGradient>
      </defs>
      <path class="top-stroke" role="img" aria-label="orange brush stroke across the top"
            d="M0 0 H1000 V30 C760 40 420 70 0 210 Z" fill="url(#topBand)"/>
      <path class="brush-stroke" role="img" aria-label="yellow and orange paint brush stroke behind the title"
            d="M230 420 C380 330 560 250 700 215 L880 280 L860 440 L920 470 L870 640 L860 900 C720 900 500 930 330 960 L120 900 L150 800 L230 740 Z"
            fill="url(#brushFill)"/>
      <rect class="crowd" role="img" aria-label="faint silhouettes of a cheering crowd with raised hands"
            x="0" y="900" width="1000" height="330" fill="url(#crowdGlow)"/>
      <path class="footer-band"
            d="M0 1175 C180 1140 330 1190 520 1160 C700 1130 860 1150 1000 1105 V1396 H0 Z"
            fill="var(--band)"/>
    </svg>

    <header class="org">
      <span class="org-mark"></span>
      <span class="org-name">HARBORLINE FELLOWSHIP</span>
    </header>

    <h1 class="title-youth">Youth</h1>
    <h2 class="title-group">Group</h2>

    <p class="schedule">SUNDAYS, 6-8PM</p>
    <p class="start-date">(Beginning April 14)</p>

    <p class="offer-lead">THERE WILL BE</p>
    <p class="offer-list">DINNER, GAMES, FRIENDS, AND A MESSAGE.</p>

    <p class="phone">91-555 218 4407</p>
    <p class="venue">Wexlander's - 4182 Quillon Ridge Ave N, Keizer, 97158</p>
    <p class="site">www.harborlinefellowship.com</p>
  </main>
</body>
</html>
```